Bright Path Consultant needs Business Card & Banner

I am a new consultant / compassionate communication trainer who needs to focus on her A-Game... Turning Tension into Understanding!

I am looking for a Business Card and Home Page Banner for my website and possible use on a Facebook Page.

I have a draft of a website (sqarespace) done (can provide the password to view) and have taken a crack at my own business cards. I have an idea what I want and need help completing.

Business name - Willow Dawn
Tag line - Turning Tension into Understanding
Vision (draft) - To cultivate harmonious relationships by building individual and organizational capacity for compassion and collaboration.
Services - I provide individual empathic coaching, interpersonal mediation and for organizations I offer collaborative communication training.

I have provided pics of me and images from my own photo stock.

Banner
I'd like the banner photo to include an image from nature and my image with my business name and tag line.

Business Card
Two sided with one of the heart images on one side and personal details on the other. Example provided.

Of course, the reason I'm hear is I need help so please feel free to improve on my ideas in any way you like.

Target Market(s)

Small to Medium sized corporations
Non-Profits
Individuals

Industry/Entity Type

Consultant

Contact Information for Business Card

Mira Dalton
Consultant (or Founder?)

Interpersonal Mediation
Collaborative Communication
phone 1-604-555-0182
mira@willowdawn.ca
www.willowdawn.ca

Requirements
Must have
• colour
• two sided
• clean lines
• strong & feminine
• canadian spellings
Nice to have
• for example see the attached pdf - WD Business Card design v4

```html
<!DOCTYPE html>
<html lang="en">
<head>
<meta charset="utf-8">
<title>Willow Dawn – Business Card</title>
<link rel="stylesheet" href="https://fonts.googleapis.com/css2?family=Open+Sans:wght@400;600;700;800&display=swap">
<style>
  :root {
    --scene-bg: #2a2a2a;
    --rose: #ec1c6b;
    --magenta: #c11f8f;
    --violet: #7a2aa6;
    --indigo: #3a3fae;
    --azure: #2a66c6;
    --flame: #f04a2a;
    --white: #ffffff;
    --ink: #111111;
    --mono-blue: #2f66c8;
    --title-pink: #f6c4dc;
    --tag-ink: #3a2330;
    --stripe-light: rgba(255, 255, 255, 0.07);
  }

  * { box-sizing: border-box; margin: 0; padding: 0; }

  html, body {
    width: 1200px;
    height: 900px;
    overflow: hidden;
    background: var(--scene-bg);
    font-family: "Open Sans", Arial, sans-serif;
  }

  .canvas {
    position: relative;
    width: 1200px;
    height: 900px;
  }

  .card {
    position: absolute;
    left: 250px;
    width: 700px;
    height: 400px;
    overflow: hidden;
    background:
      repeating-linear-gradient(155deg, transparent 0 46px, var(--stripe-light) 46px 92px),
      linear-gradient(155deg, var(--flame) 0%, var(--rose) 18%, var(--magenta) 42%, var(--violet) 66%, var(--indigo) 84%, var(--azure) 100%);
    box-shadow: 0 12px 30px rgba(0, 0, 0, 0.55);
  }

  /* Front: contact details */
  .card--front { top: 40px; }

  .card__artwork {
    position: absolute;
    left: 30px;
    top: 30px;
    width: 330px;
    height: 340px;
    background:
      radial-gradient(ellipse 45% 40% at 48% 48%, #f6e23a 0%, #f39a2a 40%, transparent 70%),
      radial-gradient(ellipse 30% 30% at 35% 35%, #e8264a 0%, transparent 70%),
      radial-gradient(ellipse 70% 70% at 50% 50%, #2a7fc8 20%, #173b8a 100%);
    box-shadow: 0 4px 10px rgba(0, 0, 0, 0.5);
  }

  .card__details {
    position: absolute;
    left: 360px;
    right: 0;
    top: 26px;
    display: flex;
    flex-direction: column;
    align-items: center;
    color: var(--white);
  }

  .monogram {
    width: 84px;
    height: 84px;
    border-radius: 50%;
    background: var(--ink);
    border: 4px solid #f27cb2;
    display: flex;
    align-items: center;
    justify-content: center;
    font-size: 34px;
    font-weight: 600;
    color: var(--mono-blue);
  }

  .person-name {
    margin-top: 14px;
    font-size: 27px;
    font-weight: 800;
    letter-spacing: 1px;
    color: var(--white);
  }

  .service {
    font-size: 18px;
    line-height: 1.5;
  }

  .service--secondary { font-size: 15px; }

  .contact-list {
    list-style: none;
    margin-top: 22px;
    align-self: flex-start;
    margin-left: 70px;
  }

  .contact-list li {
    display: flex;
    align-items: center;
    gap: 16px;
    font-size: 17px;
    margin-bottom: 12px;
  }

  .contact-list svg { width: 18px; height: 18px; fill: var(--white); flex: none; }

  /* Back: business name */
  .card--back { top: 470px; }

  .card__photo {
    position: absolute;
    left: 34px;
    top: 26px;
    width: 632px;
    height: 348px;
    background:
      radial-gradient(ellipse 30% 25% at 82% 30%, #9a9a98 0%, transparent 70%),
      radial-gradient(ellipse 40% 30% at 20% 10%, #d8d2d2 0%, transparent 70%),
      linear-gradient(180deg, #c98a9e 0%, #b85d88 45%, #3c5c9a 75%, #2f4e8a 100%);
  }

  .brand {
    position: absolute;
    left: 54px;
    right: 54px;
    top: 124px;
    text-align: center;
  }

  .brand__name {
    font-size: 64px;
    font-weight: 800;
    letter-spacing: 3px;
    color: var(--title-pink);
    line-height: 1;
    white-space: nowrap;
  }

  .brand__tagline {
    margin-top: 10px;
    font-size: 20px;
    font-weight: 700;
    letter-spacing: 1px;
    color: var(--tag-ink);
    white-space: nowrap;
  }
</style>
</head>
<body>
<main class="canvas">

  <section class="card card--front" aria-label="Business card, contact side">
    <div class="card__artwork" role="img" aria-label="Watercolour painting of a heart in red, orange and yellow on blue"></div>
    <div class="card__details">
      <div class="monogram">MD</div>
      <h1 class="person-name">MIRA DALTON</h1>
      <p class="service">Interpersonal Mediation</p>
      <p class="service service--secondary">Collaborative Communication</p>
      <ul class="contact-list">
        <li>
          <svg viewBox="0 0 24 24" aria-hidden="true"><path d="M6.6 10.8a15.1 15.1 0 0 0 6.6 6.6l2.2-2.2c.3-.3.7-.4 1-.2 1.1.4 2.3.6 3.6.6.6 0 1 .4 1 1V20c0 .6-.4 1-1 1A17 17 0 0 1 3 4c0-.6.4-1 1-1h3.5c.6 0 1 .4 1 1 0 1.3.2 2.5.6 3.6.1.3 0 .7-.2 1z"/></svg>
          <span>1 604 555 0182</span>
        </li>
        <li>
          <svg viewBox="0 0 24 24" aria-hidden="true"><path d="M12 2a10 10 0 1 0 0 20 10 10 0 0 0 0-20zm-1 17.9A8 8 0 0 1 4 12l1-.9 3 3v1a2 2 0 0 0 2 2zm6.9-2.5A2 2 0 0 0 16 16h-1v-3a1 1 0 0 0-1-1H8v-2h2a1 1 0 0 0 1-1V7h2a2 2 0 0 0 2-2v-.4a8 8 0 0 1 2.9 12.8z"/></svg>
          <span>www.willowdawn.ca</span>
        </li>
        <li>
          <svg viewBox="0 0 24 24" aria-hidden="true"><path d="M3 6h18v12H3zm2 2v.4l7 4.4 7-4.4V8zm0 2.8V16h14v-5.2l-7 4.4z"/></svg>
          <span>mira@willowdawn.ca</span>
        </li>
      </ul>
    </div>
  </section>

  <section class="card card--back" aria-label="Business card, brand side">
    <div class="card__photo" role="img" aria-label="Close-up photograph of grey river stones resting on pink and blue fabric with copper chain"></div>
    <div class="brand">
      <h2 class="brand__name">WILLOW DAWN</h2>
      <p class="brand__tagline">TURNING TENSION INTO UNDERSTANDING</p>
    </div>
  </section>

</main>
</body>
</html>
```